Solmira Coast Island Weddings, Inc.

Solmira Coast Island Weddings Business Card design for Cardovelle. Clean, contemporary, creative, colorful (using colors provided). ONE SIDE SHOULD INCLUDE logo, www.solmiracoastweddings.com, @vowsbythecove. OTHER SIDE SHOULD INCLUDE Marisol Tennant. Owner & Officiant. Corvina, Solmira Bay. 555.407.1892. marisol@solmiracoastweddings.com. Colors are blue #58AA9E
and golden #e2bf80)

Target Market(s)

Destination Wedding Clients in the United States

Contact Information for Business Card

Marisol Tennant
Owner & Officiant
Corvina, Solmira Bay
555.407.1892
marisol@solmiracoastweddings.com

Font styles to use
Sans Serif

Requirements
Must have
• Colorful (colors are blue #58AA9E
• and golden #e2bf80), clean, contemporary. ONE SIDE SHOULD INCLUDE logo, www.solmiracoastweddings.com, @vowsbythecove. Other side should include Marisol Tennant. Owner & Officiant. Corvina, Solmira Bay. 555.407.1892. marisol@solmiracoastweddings.com
Nice to have
• I would like to see a version that includes my bio photo, and one that doesn't include the bio photo

```html
<!DOCTYPE html>
<html lang="en">
<head>
<meta charset="utf-8">
<title>Solmira Coast Island Weddings – Business Card</title>
<link rel="stylesheet" href="https://fonts.googleapis.com/css2?family=Lato:wght@300;400;700;900&display=swap">
<style>
  :root {
    --backdrop: #ead9d9;
    --paper: #ffffff;
    --ink: #454545;
    --ink-soft: #555555;
    --gold: #d9b06a;
    --gold-panel: #dcbb7b;
    --rule: #9a9a9a;
    --on-gold: #ffffff;
  }
  * { box-sizing: border-box; margin: 0; padding: 0; }
  html, body { width: 1200px; height: 1040px; overflow: hidden; }
  body {
    background: var(--backdrop);
    font-family: "Lato", sans-serif;
    position: relative;
  }
  .card {
    position: absolute;
    left: 320px;
    width: 560px;
    height: 320px;
    background: var(--paper);
    box-shadow: 0 10px 24px rgba(90, 60, 60, 0.18);
  }
  .card--front { top: 110px; }
  .card--back { top: 590px; padding: 20px; }

  .front-content {
    position: absolute;
    inset: 0;
    display: flex;
    flex-direction: column;
    align-items: center;
  }
  .person-name {
    margin-top: 82px;
    font-weight: 900;
    font-size: 25px;
    letter-spacing: 2.5px;
    color: var(--ink);
    text-transform: uppercase;
  }
  .person-role {
    margin-top: 8px;
    font-weight: 700;
    font-size: 15px;
    letter-spacing: 1.5px;
    color: var(--gold);
  }
  .contact-row {
    margin-top: 26px;
    width: 440px;
    border-top: 1.5px solid var(--rule);
    border-bottom: 1.5px solid var(--rule);
    padding: 14px 4px;
    display: flex;
    justify-content: space-between;
    align-items: center;
    font-size: 15px;
    color: var(--ink-soft);
  }
  .contact-item { display: flex; align-items: center; gap: 6px; white-space: nowrap; }
  .contact-item svg { width: 14px; height: 14px; fill: var(--gold); flex: none; }
  .person-location {
    margin-top: 16px;
    font-weight: 700;
    font-size: 15px;
    letter-spacing: 1.5px;
    color: var(--gold);
  }

  .back-panel {
    width: 100%;
    height: 100%;
    background: var(--gold-panel);
    display: flex;
    flex-direction: column;
    align-items: center;
    color: var(--on-gold);
  }
  .brand-mark {
    margin-top: 50px;
    width: 64px;
    height: 64px;
    border: 2px solid var(--on-gold);
    border-radius: 50%;
  }
  .brand-name {
    margin-top: 22px;
    font-weight: 300;
    font-size: 30px;
    letter-spacing: 1.5px;
    text-align: center;
    white-space: nowrap;
  }
  .brand-links {
    margin-top: 34px;
    font-size: 14px;
    letter-spacing: 0.3px;
    white-space: nowrap;
  }
</style>
</head>
<body>
  <section class="card card--front" aria-label="Business card front">
    <div class="front-content">
      <h1 class="person-name">Marisol Tennant</h1>
      <p class="person-role">Owner &amp; Officiant</p>
      <div class="contact-row">
        <span class="contact-item">
          <svg viewBox="0 0 24 24" aria-hidden="true"><path d="M6.6 10.8a15.1 15.1 0 0 0 6.6 6.6l2.2-2.2a1 1 0 0 1 1-.25 11.4 11.4 0 0 0 3.6.57 1 1 0 0 1 1 1V20a1 1 0 0 1-1 1A17 17 0 0 1 3 4a1 1 0 0 1 1-1h3.5a1 1 0 0 1 1 1c0 1.25.2 2.45.57 3.57a1 1 0 0 1-.25 1z"/></svg>
          555.407.1892
        </span>
        <span class="contact-item">
          <svg viewBox="0 0 24 24" aria-hidden="true"><path d="M2 5h20v14H2z" fill="var(--gold)"/><path d="M2 5l10 7 10-7" fill="none" stroke="#fff" stroke-width="1.6"/></svg>
          marisol@solmiracoastweddings.com
        </span>
      </div>
      <p class="person-location">Corvina, Solmira Bay</p>
    </div>
  </section>

  <section class="card card--back" aria-label="Business card back">
    <div class="back-panel">
      <span class="brand-mark" aria-hidden="true"></span>
      <p class="brand-name">Solmira Coast Island Weddings</p>
      <p class="brand-links">www.solmiracoastweddings.com • @vowsbythecove</p>
    </div>
  </section>
</body>
</html>
```